Talented energy healer needs business card design

I need a business card design for a new energy healing business in Perth Australia. As an energy healer I am quite earthy and practical rather than floaty and fairydust.
One of the techniques I use is unique in Australia but used internationally (US, UK and Europe). I practice with Coastal Pathway Therapy, Reiki and massage as well as some other techniques I developed personally. I am starting to incorporate sound healing into my practice. I literally change people's lives. The potential for each client is wide open. A key skill I bring to my practice is the capacity for making difficult situations seem more fun and less stressful.
Clients are likely to be depressed, physically unwell, going through a difficult time, unhappy with their current situation. They are people looking for new options to solve a difficult existing problem. They have probably tried other avenues before they come to me. They are open to something different.

I would like to communicate that the client and I work together for their healing and personal growth. I would like to convey that while the work of changing is challenging it can also be fun.

Hi all, info required on the card is:

Name
Title: Healer
contact number (mobile)
I don''t have a logo - I would be interested in seeing designs that use the whole card as well as the traditional logo on one side / in one corner. Whatever ''look/feel'' I choose will carry over to the website as well.

thanks
Meg

Reason: One or two of the designs caught my eye and many appeal for different reasons, but nothing is quite right for me. I've invited a couple of other designers to contribute so I wanted to give them time to be involved. kind regards Meg

Thank you all for the fabulous designs. I really appreciated the thought that many people put into my brief and a number of designs captured important things about what I was trying to say. It was a hard choice between 3 designs in the end.
thanks again and kind regards
Meg

Target Market(s)

people looking for new options to solve a difficult existing problem

Industry/Entity Type

Massage

Logo styles of interest
Abstract Logo
Requirements
Must have
• include green and blue
Nice to have
• hands, tea / teapots , the ocean, stepping stones

```html
<!DOCTYPE html>
<html lang="en">
<head>
<meta charset="utf-8">
<title>Meg – Energy Healer Business Card</title>
<link rel="stylesheet" href="https://fonts.googleapis.com/css2?family=Arimo:ital,wght@0,400;0,700;1,700&family=Archivo+Black&family=Tinos:ital@1&display=swap">
<style>
  :root {
    --peach: #fde0c9;
    --lavender: #9d92cf;
    --green: #19994a;
    --navy: #2a2870;
    --ink: #2b2b2b;
    --white: #ffffff;
  }
  html, body {
    margin: 0;
    padding: 0;
    overflow: hidden;
    background: #ffffff;
  }
  .card {
    position: relative;
    width: 1200px;
    height: 711px;
    background: var(--peach);
    overflow: hidden;
    font-family: "Arimo", Arial, sans-serif;
  }
  .tagline-band {
    position: absolute;
    top: 0; left: 0; right: 0;
    height: 60px;
    background: var(--lavender);
    color: var(--white);
    font-weight: 700;
    font-size: 30px;
    line-height: 60px;
    text-align: right;
    padding-right: 16px;
    box-sizing: border-box;
    white-space: nowrap;
  }
  .tagline-band .arrow { margin-right: 10px; font-size: 26px; }
  .brand-name {
    position: absolute;
    left: 82px;
    top: 78px;
    color: var(--green);
    font-weight: 700;
    font-size: 72px;
    line-height: 1;
  }
  .role-badge {
    position: absolute;
    right: -40px;
    top: 104px;
    width: 232px;
    height: 104px;
    border-radius: 50%;
    background: var(--green);
    color: var(--white);
    text-align: center;
    box-sizing: border-box;
    padding: 14px 40px 0 0;
  }
  .role-badge .badge-name {
    display: block;
    font-weight: 700;
    font-size: 38px;
    line-height: 1;
  }
  .role-badge .badge-title {
    display: block;
    font-weight: 700;
    font-style: italic;
    font-size: 28px;
    line-height: 1.15;
    padding-left: 36px;
  }
  .headline {
    position: absolute;
    left: 0; right: 0;
    top: 292px;
    margin: 0;
    text-align: center;
    font-family: "Archivo Black", "Arial Black", sans-serif;
    font-weight: 400;
    font-size: 84px;
    line-height: 1;
    color: var(--navy);
    letter-spacing: 1px;
    transform: scaleY(1.3);
    transform-origin: center top;
  }
  .motto {
    position: absolute;
    top: 418px;
    left: 321px;
    width: 585px;
    display: flex;
    justify-content: space-between;
    align-items: center;
    color: var(--navy);
    font-weight: 700;
    font-size: 34px;
    line-height: 40px;
  }
  .motto .rule {
    width: 118px;
    height: 7px;
    background: var(--green);
  }
  .contact-line {
    position: absolute;
    left: 680px;
    top: 586px;
    font-family: "Tinos", "Times New Roman", serif;
    font-style: italic;
    font-size: 56px;
    color: var(--ink);
    white-space: nowrap;
  }
  .web-band {
    position: absolute;
    left: 0; right: 0; bottom: 0;
    height: 62px;
    background: var(--green);
    color: var(--white);
    font-weight: 700;
    font-size: 36px;
    line-height: 62px;
    text-align: right;
    padding-right: 14px;
    box-sizing: border-box;
  }
</style>
</head>
<body>
  <main class="card">
    <div class="tagline-band"><span class="arrow">&#10148;</span>Difficult situations seem more Fun and less Stressful</div>

    <div class="brand-name">Meg</div>

    <div class="role-badge">
      <span class="badge-name">Meg</span>
      <span class="badge-title">Director</span>
    </div>

    <h1 class="headline">ENERGY HEALER</h1>

    <div class="motto">
      <span class="rule" aria-hidden="true"></span>
      <span class="motto-text">We Do It Together</span>
      <span class="rule" aria-hidden="true"></span>
    </div>

    <div class="contact-line">Call......................</div>

    <div class="web-band">www.coastalpathway.com.au.</div>
  </main>
</body>
</html>
```